Stem Cell Injections

We are making a brochure for injecting stem cells into joints tendons and muscles to repair chronic and acute injuries.
i need a six page brochure
velumarq.com name of website
web sites that have similar feel are
http://www.tavicore.com/lumivaxx-procedures/
http://www.brindlova.com/stemcelltreatments/rheumatoidarthritisstemcelltreatment.html
http://www.brindlova.com/stemcellvideos/orthopedicstemcelltherapy.html
http://thewexholtclinic.com/bone-marrow-cell-concentrate-platelet-rich-plasma.asp
Requirements
Must have
- Graphics of injections into joints, tendons and muscle showing injections
for ideas please google image search "joint injections"
Nice to have
- we need personal bios of both doctors that do the procedures.
Should not have
- should look very modern not classic or old

```html
<!DOCTYPE html>
<html lang="en">
<head>
<meta charset="utf-8">
<title>Platelet-Rich Plasma and Bone Marrow Cell Concentrate</title>
<link rel="stylesheet" href="https://fonts.googleapis.com/css2?family=Cabin:wght@400;700&family=Tinos:wght@700&display=swap">
<style>
  :root {
    --navy: #34427a;
    --ink: #2f3d7c;
    --paper: #ffffff;
    --photo-light: #eef3f6;
    --photo-mid: #d3dde3;
    --photo-deep: #b9c4cc;
  }
  * { margin: 0; padding: 0; box-sizing: border-box; }
  html, body { width: 928px; height: 1200px; overflow: hidden; background: var(--paper); }
  .page {
    position: relative;
    width: 928px;
    height: 1200px;
    font-family: "Cabin", "Gill Sans", sans-serif;
    color: var(--ink);
  }
  .hero-photo {
    position: absolute;
    left: 0; top: 0;
    width: 928px; height: 440px;
    background:
      radial-gradient(ellipse 260px 320px at 820px 200px, var(--photo-deep) 0%, rgba(185,196,204,0) 70%),
      linear-gradient(180deg, var(--photo-mid) 0%, var(--photo-light) 55%, var(--paper) 100%);
  }
  .title-band {
    position: absolute;
    left: 0; top: 426px;
    width: 542px; height: 98px;
    background: var(--navy);
    padding: 25px 0 0 44px;
  }
  .title-band h1 {
    font-family: "Tinos", "Times New Roman", serif;
    font-weight: 700;
    font-size: 22.5px;
    line-height: 21.5px;
    color: var(--paper);
  }
  .intro {
    position: absolute;
    left: 43px;
    width: 500px;
  }
  .intro h2 {
    font-weight: 700;
    font-size: 21px;
    line-height: 22px;
    margin-bottom: 17px;
  }
  .intro p {
    font-size: 16px;
    line-height: 18.2px;
  }
  .intro-prp { top: 556px; }
  .intro-bmcc { top: 945px; }
  .conditions {
    position: absolute;
    left: 583px; top: 426px;
    width: 301px; height: 730px;
    background: var(--navy);
    color: var(--paper);
    padding: 27px 10px 0 33px;
  }
  .conditions h3 {
    font-weight: 700;
    font-size: 15.5px;
    line-height: 18.4px;
    margin-bottom: 1px;
  }
  .conditions ul { list-style: none; }
  .conditions li {
    position: relative;
    padding-left: 21px;
    font-size: 15.5px;
    line-height: 18.2px;
  }
  .conditions li::before {
    content: "";
    position: absolute;
    left: 4px; top: 7px;
    width: 4px; height: 4px;
    border-radius: 50%;
    background: var(--paper);
  }
</style>
</head>
<body>
<div class="page">
  <div class="hero-photo" role="img" aria-label="Photo of a doctor in a white coat with a stethoscope holding up a syringe in a bright clinic"></div>

  <div class="title-band">
    <h1>Platelet-Rich Plasma (PRP) and<br>Bone Marrow Cell Concentrate (BMCC)</h1>
  </div>

  <section class="intro intro-prp">
    <h2>What is Platelet-Rich Plasma<br>(PRP)</h2>
    <p>Platelet-rich plasma or PRP is an "autologous blood therapy" that uses a patient's own blood components to stimulate a healing response in damaged tissues. In response to an injury or tissue damage, your body naturally recruits platelets and white blood cells from the blood to initiate a healing response. Under normal conditions, platelets store numerous growth factors which are released in response to signals from the injured tissue. Modern technology allows us to concentrate platelets and white blood cells from your blood, and induce this growth factor release as we inject the solution directly into injured tissue, simulating this same healing response in a more powerful form. By enhancing the body's natural healing capacity, the treatment may lead to a more rapid, more efficient, and more thorough restoration of the tissue to a healthy state.</p>
  </section>

  <section class="intro intro-bmcc">
    <h2>What is Bone Marrow Cell Concentrate (BMCC)</h2>
    <p>It is well established that a significant population of our bodies' stem cells are contained within our bone marrow. By harvesting blood and tissue from the bone marrow space of the hip, an injectable product can be produced by concentrating platelets and cells withdrawn through a simple outpatient needle aspiration procedure, done with local anesthetic and light sedation. BMCC contains all of the growth and healing factors in PRP, along with concentrated "pluripotent" or stem-like cells which further contribute to the regenerative process.</p>
  </section>

  <aside class="conditions">
    <h3>What conditions can be treated with PRP and BMCC?</h3>
    <ul>
      <li>Knee Pain</li>
      <li>Tendon Injuries (Patellar Tendonitis, Quad Tendon)</li>
      <li>Muscle injuries</li>
      <li>Ligament sprains or tears (MCL, LCL)</li>
      <li>Bursitis</li>
      <li>Osteoarthritis</li>
      <li>Hip Pain</li>
      <li>Muscle pain or injury</li>
      <li>Pyriformis syndrome</li>
      <li>Greater Trochanteric Bursitis</li>
      <li>Tendon Injuries</li>
      <li>Sacroiliac joint pain</li>
      <li>Hamstring tendonitis or tears</li>
      <li>Osteoarthritis</li>
      <li>Shoulder and Arm Pain</li>
      <li>Rotator Cuff tendonitis, tendonopathy or partial tears</li>
      <li>Bicipital tendonitis</li>
      <li>Medial and Lateral epicondylitis (golfers &amp; tennis elbow)</li>
      <li>Ulnar Collateral Ligament sprain or tear</li>
      <li>Lower Leg and Foot Pain</li>
      <li>Plantar Fasciitis</li>
      <li>Shin Splints</li>
      <li>Peroneal tendonitis</li>
      <li>Ankle sprains/ligament injury</li>
      <li>Achilles tendonitis or partial tears</li>
    </ul>
  </aside>
</div>
</body>
</html>
```